lotus bowl vietnamese restaurant in need of a new menu

a family owned vietnamese restaurant in need of a new menu design that is fun, classy, and yet simple. menu that will catch the customers eyes. easy to read yet flows nicely. like to use the color green (basil green color) creme yellow and maroon. open to other colors as long as it looks nice together. our restaurant is family oriented, casual yet has a nice ambiance atmosphere.
prefer 11x17 portrait double sided. attached is our menu with the current price updated so use the info on this to start creating! looking for something unique, professional and one of a kind menu!
please use your own creative layout and design. we are open to ideas. the files uploaded are the updated prices and the logo is to use whichever one you feel goes with the menu.
Reason: don't see anything we like so far...please be creative!
Target Market(s)
restaurant consumers
Industry/Entity Type
Restaurant
Look and feel

```html
<!DOCTYPE html>
<html lang="en">
<head>
<meta charset="utf-8">
<title>Lotus Bowl – Menu</title>
<link rel="stylesheet" href="https://fonts.googleapis.com/css2?family=Bebas+Neue&family=Lato:wght@700&family=Oswald:wght@300;400;500&display=swap">
<style>
  :root {
    --basil: #6cbf3f;
    --basil-soft: #8fd36b;
    --basil-light: #b5e39a;
    --ink: #222222;
    --leaf-ink: #1d2a12;
    --paper: #ffffff;
  }
  * { margin: 0; padding: 0; box-sizing: border-box; }
  html, body { width: 1200px; height: 777px; overflow: hidden; background: var(--paper); }
  .menu-sheet { position: relative; width: 1200px; height: 777px; font-family: "Oswald", sans-serif; color: var(--ink); }

  .veg-panel {
    position: absolute; left: 0; top: 0; width: 398px; height: 334px;
    background: radial-gradient(ellipse at 30% 40%, var(--basil-light), var(--basil-soft) 60%, var(--basil) 100%);
  }
  .section-title { position: absolute; font-family: "Bebas Neue", sans-serif; font-weight: 400; line-height: 1; letter-spacing: 1px; }
  .veg-title { left: 0; width: 398px; top: 20px; text-align: center; font-size: 50px; color: var(--leaf-ink); }
  .veg-subtitle { position: absolute; left: 0; width: 398px; top: 69px; text-align: center; font-weight: 300; font-size: 9px; letter-spacing: .5px; color: var(--leaf-ink); }
  .roll-plate { position: absolute; left: 250px; top: 100px; width: 140px; height: 140px; border-radius: 50%;
    background: radial-gradient(circle at 60% 60%, #5a2e16 0 22%, #f2ece0 23% 42%, #c89a5c 43% 100%); }

  .menu-item { position: absolute; z-index: 2; padding-left: 17px; line-height: 12px; white-space: nowrap; }
  .item-num { position: absolute; left: 0; top: 0; font-weight: 400; font-size: 10.5px; line-height: 12px; }
  .item-name { font-weight: 500; font-size: 10.5px; text-transform: uppercase; }
  .item-price { font-weight: 300; font-style: italic; font-size: 10.5px; color: var(--basil); margin-left: 4px; }
  .veg-panel .item-price { color: var(--leaf-ink); }
  .item-desc, .soda-list { display: block; font-weight: 300; font-size: 8.2px; line-height: 11px; text-transform: uppercase; }

  .bev-title { left: 132px; top: 342px; font-size: 52px; color: var(--basil); }

  .flavor-list { position: absolute; z-index: 2; top: 684px; font-weight: 300; font-size: 8.4px; line-height: 12px; text-transform: uppercase; list-style: none; }
  .flavor-list li::before { content: "• "; }

  .photo { position: absolute; z-index: 1; }
  .coffee-filter { left: 316px; top: 550px; width: 76px; height: 146px; border-radius: 6px 6px 30px 30px;
    background: linear-gradient(#3a3a3a 0 26%, #ffffff 27% 52%, #3b2416 53% 68%, #efe3c8 69% 82%, #f6f6f6 83%); }
  .thai-tea { left: 198px; top: 636px; width: 56px; height: 124px; border-radius: 4px 4px 10px 10px;
    background: linear-gradient(#f1f1f1 0 6%, #e8782c 7% 70%, #f3c08f 71%); }
  .three-color { left: 259px; top: 640px; width: 54px; height: 118px; border-radius: 4px 4px 10px 10px;
    background: linear-gradient(#f6f6f6 0 22%, #3dbb8a 23% 45%, #e8d54c 46% 62%, #1c2a1a 63%); }

  .brand-name { position: absolute; font-family: "Lato", sans-serif; font-weight: 700; color: var(--ink); white-space: nowrap; }
  .brand-mark { display: inline-block; background: var(--basil); vertical-align: middle; }
  .brand-fold { left: 503px; top: 326px; font-size: 26px; }
  .brand-fold .brand-mark { width: 12px; height: 12px; margin-right: 8px; }
  .brand-cover { left: 846px; top: 520px; font-size: 42px; }
  .brand-cover .brand-mark { width: 18px; height: 18px; margin-right: 12px; }

  .cover-art { position: absolute; left: 800px; top: 0; }

  .contact { position: absolute; left: 822px; top: 711px; font-weight: 400; font-size: 13.5px; line-height: 17px; text-transform: uppercase; list-style: none; }
  .contact li { display: flex; align-items: center; gap: 6px; }
  .contact svg { width: 10px; height: 12px; fill: var(--basil); }
</style>
</head>
<body>
<main class="menu-sheet">

  <section class="veg-panel" aria-label="Vegetarian plates">
    <h2 class="section-title veg-title">Mon Chay</h2>
    <p class="veg-subtitle">VEGETARIAN PLATE</p>
    <div class="photo roll-plate" role="img" aria-label="Photo of tofu spring rolls on a woven tray with dipping sauce"></div>

    <div class="menu-item" style="left:42px;top:88px"><span class="item-num">64.</span><span class="item-name">Goi Cuon Tofu</span><span class="item-price">4.50</span><span class="item-desc">Fried tofu spring roll</span></div>
    <div class="menu-item" style="left:42px;top:117px"><span class="item-num">65.</span><span class="item-name">Soup Rau Cai</span><span class="item-price">(S) 3.00 (L) 5.95</span><span class="item-desc">Vegetables soup</span></div>
    <div class="menu-item" style="left:42px;top:147px"><span class="item-num">66.</span><span class="item-name">Pho Dau Hu Rau Cai</span><span class="item-price">9.50</span><span class="item-desc">Fried tofu and vegetables noodle soup</span></div>
    <div class="menu-item" style="left:42px;top:176px"><span class="item-num">67.</span><span class="item-name">Dau Hu Xao Rau Cai</span><span class="item-price">9.95</span><span class="item-desc">Stir fry fried tofu with mixed vegetables</span></div>
    <div class="menu-item" style="left:42px;top:206px"><span class="item-num">68.</span><span class="item-name">Dau Hu Xao Xa Ot</span><span class="item-price">9.95</span><span class="item-desc">Stir fry fried tofu with hot chilli and lemongrass</span></div>
    <div class="menu-item" style="left:42px;top:233px"><span class="item-num">69.</span><span class="item-name">Bun Xao Dau Hu Rau Cai</span><span class="item-price">9.50</span><span class="item-desc">Stir fry fried vermecelli with fried tofu and mixed vegetables</span></div>
    <div class="menu-item" style="left:42px;top:261px"><span class="item-num">70.</span><span class="item-name">Com Chien Dau Hu Rau Cai</span><span class="item-price">9.50</span><span class="item-desc">Fried tofu and vegetables fried rice</span></div>
    <div class="menu-item" style="left:42px;top:288px"><span class="item-num">71.</span><span class="item-name">Bun Dau Hu</span><span class="item-price">9.25</span><span class="item-desc">Fried tofu vermicelli bowl</span></div>
  </section>

  <section class="beverages" aria-label="Beverages">
    <h2 class="section-title bev-title">Beverages</h2>

    <div class="menu-item" style="left:42px;top:399px"><span class="item-num">72.</span><span class="item-name">Nuoc Ngot - Soda</span><span class="item-price">1.50</span>
      <span class="soda-list">• Fizz Cola • Diet Fizz • Fizz Zero • Pop Cola • Summit Mist • Sunburst • Dr. Spice</span>
      <span class="soda-list">• Lemon Spark • Club Soda • Gingerale • Root Beer • Bottle Water</span></div>
    <div class="menu-item" style="left:42px;top:440px"><span class="item-num">73.</span><span class="item-name">Nuoc Dua</span><span class="item-price">4.25</span><span class="item-desc">Fresh coconut juice</span></div>
    <div class="menu-item" style="left:42px;top:469px"><span class="item-num">74.</span><span class="item-name">Cam Vat</span><span class="item-price">4.00</span><span class="item-desc">Fresh orange juice</span></div>
    <div class="menu-item" style="left:42px;top:499px"><span class="item-num">75.</span><span class="item-name">Da Chanh</span><span class="item-price">3.50</span><span class="item-desc">Fresh limeade juice</span></div>
    <div class="menu-item" style="left:42px;top:528px"><span class="item-num">76.</span><span class="item-name">Soda Da Chanh</span><span class="item-price">4.00</span><span class="item-desc">Fresh limeade with club soda</span></div>
    <div class="menu-item" style="left:42px;top:556px"><span class="item-num">77.</span><span class="item-name">Thai Ice Tea</span><span class="item-price">4.00</span><span class="item-desc">Thai tea mix with half &amp; half milk</span></div>
    <div class="menu-item" style="left:42px;top:584px"><span class="item-num">78.</span><span class="item-name">Alpine Sparking</span><br><span class="item-name">Mineral Water</span><span class="item-price">1.95</span></div>
    <div class="menu-item" style="left:42px;top:612px"><span class="item-num">79.</span><span class="item-name">Cafe Sua Da or Den Da</span><span class="item-price">1.95</span><span class="item-desc">Vietnamese milk ice coffee or<br>black coffee (hot or cold)</span></div>

    <div class="menu-item" style="left:211px;top:456px"><span class="item-num">80.</span><span class="item-name">Chan Muoi</span><span class="item-price">3.50</span><span class="item-desc">Salty brined lime juice</span></div>
    <div class="menu-item" style="left:211px;top:485px"><span class="item-num">81.</span><span class="item-name">Soda Chan Muoi</span><span class="item-price">4.25</span><span class="item-desc">Salty brined lime juice with club soda</span></div>
    <div class="menu-item" style="left:211px;top:515px"><span class="item-num">82.</span><span class="item-name">Sua Hot Ga</span><span class="item-price">4.25</span><span class="item-desc">Sweet milk &amp; egg with club soda</span></div>
    <div class="menu-item" style="left:211px;top:544px"><span class="item-num">83.</span><span class="item-name">Sau Hot Ga</span><span class="item-price">4.25</span><span class="item-desc">Soy bean milk</span></div>
    <div class="menu-item" style="left:211px;top:572px"><span class="item-num">84.</span><span class="item-name">Tra Da</span><span class="item-price">1.50</span><span class="item-desc">Unsweetened ice tea</span></div>
    <div class="menu-item" style="left:211px;top:600px"><span class="item-num">85.</span><span class="item-name">Che 3 Mau</span><span class="item-price">3.50</span><span class="item-desc">Vietnamese 3 color dessert</span></div>

    <div class="photo coffee-filter" role="img" aria-label="Photo of Vietnamese drip coffee filter over a glass of milk coffee"></div>
    <div class="photo thai-tea" role="img" aria-label="Photo of a glass of Thai iced tea"></div>
    <div class="photo three-color" role="img" aria-label="Photo of a glass of three color dessert"></div>

    <div class="menu-item" style="left:42px;top:666px"><span class="item-num">86.</span><span class="item-name">Sinh To - Pearl Smoothies</span><span class="item-price">4.50</span></div>
    <ul class="flavor-list" style="left:62px"><li>Avocado</li><li>Durian</li><li>Coconut</li></ul>
    <ul class="flavor-list" style="left:129px"><li>Banana</li><li>Strawberry</li><li>Taro</li></ul>
    <ul class="flavor-list" style="left:203px"><li>Honeydew</li><li>Green Tea</li><li>Thai Tea</li></ul>
  </section>

  <p class="brand-name brand-fold"><span class="brand-mark"></span>Lotus Bowl</p>

  <svg class="cover-art" width="400" height="440" viewBox="0 0 400 440">
    <defs>
      <radialGradient id="phoTones" cx="60%" cy="40%" r="75%">
        <stop offset="0" stop-color="#a9cf6a"/>
        <stop offset="0.45" stop-color="#6ea83c"/>
        <stop offset="0.7" stop-color="#c23a2c"/>
        <stop offset="1" stop-color="#7a5a40"/>
      </radialGradient>
    </defs>
    <path role="img" aria-label="Photo of a red bowl of chicken pho with fresh herbs, jalapeño and lime"
          d="M0,0 H400 V378 Q320,428 230,424 Q90,412 0,296 Z" fill="url(#phoTones)"/>
    <path d="M0,306 Q95,422 230,432 Q320,436 400,388" fill="none" stroke="var(--basil)" stroke-width="3"/>
  </svg>

  <p class="brand-name brand-cover"><span class="brand-mark"></span>Lotus Bowl</p>

  <ul class="contact">
    <li><svg viewBox="0 0 10 12"><path d="M2,0.5 L3.8,0.5 L4.6,3.2 L3.4,4.2 Q4.4,6.8 6.6,8 L7.6,6.8 L10,7.8 L10,9.8 Q9.4,11.6 7.6,11.4 Q1.2,9.6 0.4,2.4 Q0.6,0.7 2,0.5 Z"/></svg>(555) 204-3187</li>
    <li><svg viewBox="0 0 10 12"><path d="M5,0 A4.6,4.6 0 0 1 9.6,4.6 Q9.6,7.6 5,12 Q0.4,7.6 0.4,4.6 A4.6,4.6 0 0 1 5,0 Z M5,2.6 A2,2 0 1 0 5,6.6 A2,2 0 1 0 5,2.6 Z" fill-rule="evenodd"/></svg>1280 Willow Creek Blvd Maple Grove, FL 30000</li>
  </ul>

</main>
</body>
</html>
```